BrackenfieldGoods.com

I need a site that I can sell dewatering equipment to the construction industry.
Ie, pipes fittings pumps and other such things needed to remove the groundwater on construction sites. Here in Florida, it’s needed almost everywhere seeing we are at sea level.
I want to be able to sell these products on the site and receive

Coding

Coded - Design and coding required

Number of Pages Required

1 page

```html
<!DOCTYPE html>
<html lang="en">
<head>
<meta charset="utf-8">
<title>Brackenfield Goods llc — Dewatering Equipment</title>
<link rel="stylesheet" href="https://fonts.googleapis.com/css2?family=Oswald:wght@300;400;500;600&family=Roboto+Condensed:wght@300;400;700&display=swap">
<style>
:root{
  --orange:#ff5a1f;
  --navy:#14202b;
  --slate:#2f3941;
  --light:#f1f1f1;
  --white:#ffffff;
  --ink:#222222;
  --muted:#6b6b6b;
  --grey-word:#8a8a8a;
}
*{margin:0;padding:0;box-sizing:border-box}
html,body{width:1200px;height:3835px;overflow:hidden}
body{font-family:"Roboto Condensed",Arial,sans-serif;color:var(--ink);background:var(--white);position:relative}
.section{position:absolute;left:0;width:1200px}
.heading{font-family:"Oswald",Arial,sans-serif;font-weight:500;font-size:22px;text-align:center;letter-spacing:.5px;text-transform:uppercase}
.rule{width:260px;height:4px;background:var(--orange);margin:12px auto 0}
.sub{font-size:11px;text-align:center;color:var(--muted);margin-top:12px}

/* top bar */
.topbar{top:0;height:44px;background:var(--navy);color:#cfd6dc;font-size:11px;display:flex;justify-content:flex-end;align-items:center;gap:28px;padding-right:210px}
.topbar span::before{content:"";display:inline-block;width:7px;height:7px;background:var(--orange);margin-right:6px;vertical-align:middle}

/* header */
.header{top:44px;height:92px;background:var(--white);display:flex;align-items:center}
.brand{font-family:"Roboto Condensed",Arial,sans-serif;font-size:26px;font-weight:400;margin-left:50px;width:415px}
.nav{display:flex;gap:22px;font-family:"Oswald",Arial,sans-serif;font-size:14px;font-weight:500;text-transform:uppercase}
.search{position:absolute;left:926px;top:0;width:104px;height:92px;background:var(--orange);display:flex;align-items:center;justify-content:center}

/* hero */
.hero{top:136px;height:498px;background:linear-gradient(135deg,#5a4a3e,#3b342f 45%,#6a5444);color:var(--white);text-align:center}
.hero h1{font-family:"Oswald",Arial,sans-serif;font-weight:600;font-size:46px;color:var(--orange);position:absolute;top:160px;width:100%}
.hero p{position:absolute;top:244px;left:260px;width:680px;font-size:16px;line-height:19px}
.arrow{position:absolute;top:219px;width:57px;height:57px;border:2px solid rgba(255,255,255,.7);display:flex;align-items:center;justify-content:center}

/* features */
.features{top:634px;height:279px;background:var(--light)}
.feature{position:absolute;top:76px;width:220px;text-align:center}
.feature h3{font-family:"Oswald",Arial,sans-serif;font-weight:500;font-size:20px;margin-top:18px}
.feature p{font-size:10px;color:var(--muted);line-height:13px;margin-top:6px}

/* about */
.about{top:913px;height:498px}
.about .heading{margin-top:42px}
.who{position:absolute;left:91px;top:157px;width:365px}
.who h4{font-family:"Oswald",Arial,sans-serif;font-weight:500;font-size:20px}
.who .line{width:260px;height:3px;background:var(--orange);margin-top:12px}
.who p{font-size:10.5px;line-height:13px;color:var(--muted);margin-top:16px}
.btn{display:inline-block;background:var(--orange);color:var(--white);font-family:"Oswald",Arial,sans-serif;font-size:13px;padding:14px 0;width:152px;text-align:center;margin-top:14px}
.video{position:absolute;left:629px;top:165px;width:480px;height:263px;background:#000}

/* offer */
.offer{top:1411px;height:499px;background:var(--orange);color:var(--white)}
.offer .heading{margin-top:48px}
.offer .rule{background:var(--white)}
.offer .sub{color:#ffe2d6}
.card{position:absolute;top:160px;width:315px;height:263px;background:var(--white);color:var(--ink);text-align:center}
.card .photo{height:161px;background:linear-gradient(180deg,#a9b7c4,#7a7560 55%,#9a8a6a)}
.card h3{font-family:"Oswald",Arial,sans-serif;font-weight:400;font-size:22px;margin-top:16px}
.card p{font-size:10px;color:var(--muted);line-height:13px;margin:6px 50px 0}

/* products */
.products{top:1910px;height:495px;background:var(--slate);color:var(--white)}
.products .heading{margin-top:42px}
.products .sub{color:#c3c9ce}
.filters{display:flex;justify-content:center;gap:18px;margin-top:40px;font-family:"Oswald",Arial,sans-serif;font-size:10px;text-transform:uppercase;align-items:center}
.filters .on{border:2px solid var(--orange);padding:4px 6px}
.prod{position:absolute;top:198px;width:342px;height:212px;background:linear-gradient(135deg,#5b2a24,#a8352a 50%,#3b3b3b)}
.prod.active{background:rgba(255,90,31,.85);text-align:center}
.prod.active h3{font-family:"Oswald",Arial,sans-serif;font-size:22px;font-weight:400;margin-top:96px}
.prod.active p{font-size:10px;line-height:13px;margin:4px 80px 0}

/* gallery */
.gallery{top:2405px;height:613px}
.gallery .heading{margin-top:54px}
.grid{position:absolute;top:196px;left:0;display:grid;grid-template-columns:repeat(4,300px);grid-template-rows:repeat(2,208px)}
.tile{background:linear-gradient(160deg,#c9b79a,#8c7a5e)}

/* partners */
.partners{top:3018px;height:282px;background:var(--light)}
.partners .heading{margin-top:40px}
.logos{position:absolute;top:165px;left:0;width:1200px}
.logos span{position:absolute;transform:translateX(-50%);font-family:"Oswald",Arial,sans-serif;font-size:60px;color:var(--grey-word);letter-spacing:1px}

/* cta */
.cta{top:3300px;height:183px;background:var(--orange);color:var(--white)}
.cta h2{position:absolute;left:73px;top:62px;font-family:"Roboto Condensed",Arial,sans-serif;font-weight:700;font-size:19px}
.cta p{position:absolute;left:73px;top:92px;width:780px;font-size:11.5px;line-height:14px}
.cta .dark{position:absolute;left:913px;top:65px;width:201px;height:58px;background:#111;display:flex;align-items:center;justify-content:center;font-family:"Oswald",Arial,sans-serif;font-size:15px}

/* footer */
.footer{top:3483px;height:352px;background:linear-gradient(180deg,#3e464d,#2c3339);color:#e4e7ea}
.col{position:absolute;top:73px;font-size:13.5px;line-height:18px}
.col h5{font-family:"Oswald",Arial,sans-serif;font-weight:400;font-size:14px;text-transform:uppercase;margin-bottom:16px}
.footer .base{position:absolute;bottom:0;left:0;width:1200px;height:26px;background:#1d2227}
</style>
</head>
<body>

<div class="section topbar">
  <span>+1 (555) 014 0216</span><span>info@brackenfieldgoods.com</span><span>Mon - Sat 10:00 - 20:00</span>
</div>

<header class="section header">
  <div class="brand">Brackenfield Goods llc</div>
  <nav class="nav"><span>Home</span><span>About us</span><span>Offer</span><span>Products</span><span>Gallery</span><span>Contact us</span></nav>
  <div class="search">
    <svg width="34" height="34" viewBox="0 0 34 34"><circle cx="14" cy="14" r="10" fill="none" stroke="#fff" stroke-width="4"/><line x1="21" y1="21" x2="31" y2="31" stroke="#fff" stroke-width="4" stroke-linecap="round"/></svg>
  </div>
</header>

<section class="section hero" role="img" aria-label="Worker beside a red dewatering pump on an excavated construction site">
  <div class="arrow" style="left:47px"><svg width="20" height="28"><polyline points="15,3 5,14 15,25" fill="none" stroke="#fff" stroke-width="2"/></svg></div>
  <div class="arrow" style="left:1096px"><svg width="20" height="28"><polyline points="5,3 15,14 5,25" fill="none" stroke="#fff" stroke-width="2"/></svg></div>
  <h1>WELCOME TO</h1>
  <p>Lorem ipsum dolor sit amet, consectetur adipiscing elit. Praesent porttitor urna eu eleifend commodo. Curabitur rutrum, sem vel convallis posuere, lacus libero pharetra mi, sit amet maximus dui orci ut dolor. Mauris a consectetur elit. Pellentesque pulvinar vitae sapien ac semper. Morbi interdum finibus eros in interdum. Aliquam eu facilisis orci, et semper velit. Morbi justo nisi, maximus id dignissim a, viverra ac tortor. Cras vel faucibus augue, sed viverra magna. Suspendisse a commodo elit.</p>
</section>

<section class="section features">
  <div class="feature" style="left:88px">
    <svg width="64" height="50" viewBox="0 0 64 50"><rect x="4" y="18" width="56" height="14" fill="#ff5a1f"/><rect x="8" y="10" width="8" height="30" fill="#ff5a1f"/><rect x="48" y="10" width="8" height="30" fill="#ff5a1f"/><rect x="28" y="4" width="8" height="14" fill="#ff5a1f"/><rect x="22" y="2" width="20" height="5" fill="#ff5a1f"/></svg>
    <h3>Lorem Ipsun</h3><p>Lorem ipsum dolor sit amet, consectetur adipiscing elit, sed do eiusmod</p>
  </div>
  <div class="feature" style="left:331px">
    <svg width="50" height="50" viewBox="0 0 50 50"><path d="M8 24a17 17 0 0 1 34 0z" fill="#ff5a1f"/><rect x="5" y="23" width="40" height="5" fill="#ff5a1f"/><path d="M8 50c0-10 8-16 17-16s17 6 17 16z" fill="#ff5a1f"/></svg>
    <h3>Praesent porttitor urna</h3><p>Lorem ipsum dolor sit amet, consectetur adipiscing elit, sed do eiusmod</p>
  </div>
  <div class="feature" style="left:589px">
    <svg width="50" height="50" viewBox="0 0 50 50"><path d="M40 4a10 10 0 0 0-12 13L6 39l5 5 22-22a10 10 0 0 0 13-12l-6 6-5-1-1-5z" fill="#ff5a1f"/></svg>
    <h3>Curabitur rutrum</h3><p>Lorem ipsum dolor sit amet, consectetur adipiscing elit, sed do eiusmod</p>
  </div>
  <div class="feature" style="left:853px">
    <svg width="60" height="50" viewBox="0 0 60 50"><rect x="4" y="24" width="30" height="14" fill="#ff5a1f"/><rect x="14" y="14" width="14" height="12" fill="#ff5a1f"/><polyline points="30,22 44,6 56,26" fill="none" stroke="#ff5a1f" stroke-width="4"/><rect x="2" y="40" width="34" height="7" rx="3.5" fill="#ff5a1f"/></svg>
    <h3>Morbi interdum finibus</h3><p>Lorem ipsum dolor sit amet, consectetur adipiscing elit, sed do eiusmod</p>
  </div>
</section>

<section class="section about">
  <h2 class="heading">About us</h2><div class="rule"></div>
  <p class="sub">Lorem ipsum dolor sit amet, consectetur adipiscing elit. Praesent porttitor urna eu eleifend commodo.</p>
  <div class="who">
    <h4>WHO WE ARE</h4><div class="line"></div>
    <p>Lorem ipsum dolor sit amet, consectetur adipiscing elit. Praesent porttitor urna eu eleifend commodo. Curabitur rutrum, sem vel convallis posuere, lacus libero pharetra mi, sit amet maximus dui orci ut dolor. Mauris a consectetur elit. Pellentesque pulvinar vitae sapien ac semper. Morbi interdum finibus eros in interdum. Aliquam eu facilisis orci, et semper velit. Morbi justo nisi, maximus id dignissim a, viverra ac tortor. Cras vel faucibus augue, sed viverra magna. Suspendisse a commodo elit.</p>
    <span class="btn">CONTACT NOW</span>
  </div>
  <div class="video" role="img" aria-label="Company video"></div>
</section>

<section class="section offer">
  <h2 class="heading">What we offer</h2><div class="rule"></div>
  <p class="sub">Lorem ipsum dolor sit amet, consectetur adipiscing elit. Praesent porttitor urna eu eleifend commodo.</p>
  <div class="card" style="left:91px"><div class="photo" role="img" aria-label="Yellow loader moving sand on a site"></div><h3>Lorem Ipsun</h3><p>Lorem ipsum dolor sit amet, consectetur adipiscing elit, sed do eiusmod</p></div>
  <div class="card" style="left:443px"><div class="photo" role="img" aria-label="Drilling rig installing well points"></div><h3>Lorem Ipsun</h3><p>Lorem ipsum dolor sit amet, consectetur adipiscing elit, sed do eiusmod</p></div>
  <div class="card" style="left:794px"><div class="photo" role="img" aria-label="Drained concrete slab excavation"></div><h3>Lorem Ipsun</h3><p>Lorem ipsum dolor sit amet, consectetur adipiscing elit, sed do eiusmod</p></div>
</section>

<section class="section products">
  <h2 class="heading">Our products</h2><div class="rule"></div>
  <p class="sub">Lorem ipsum dolor sit amet, consectetur adipiscing elit. Praesent porttitor urna eu eleifend commodo.</p>
  <div class="filters"><span class="on">All</span><span>Pumps</span><span>Generators</span><span>Dewatering</span><span>Plate compactors</span><span>Light towers</span></div>
  <div class="prod active" style="left:86px" role="img" aria-label="Orange diesel generator">
    <svg style="position:absolute;left:153px;top:50px" width="36" height="36" viewBox="0 0 36 36"><circle cx="15" cy="15" r="11" fill="none" stroke="#fff" stroke-width="3.5"/><line x1="23" y1="23" x2="33" y2="33" stroke="#fff" stroke-width="4" stroke-linecap="round"/></svg>
    <h3>Lorem Ipsun</h3><p>Lorem ipsum dolor sit amet, consectetur adipiscing elit, sed do eiusmod</p>
  </div>
  <div class="prod" style="left:428px" role="img" aria-label="Red trailer-mounted dewatering pump"></div>
  <div class="prod" style="left:770px;width:344px" role="img" aria-label="Red skid-mounted pump engine"></div>
</section>

<section class="section gallery">
  <h2 class="heading">Gallery</h2><div class="rule"></div>
  <p class="sub">Lorem ipsum dolor sit amet, consectetur adipiscing elit. Praesent porttitor urna eu eleifend commodo.</p>
  <div class="grid">
    <div class="tile" style="background:rgba(220,120,70,.9);display:flex;align-items:center;justify-content:center" role="img" aria-label="Excavated site with well points">
      <svg width="46" height="46" viewBox="0 0 46 46"><circle cx="19" cy="19" r="14" fill="none" stroke="#fff" stroke-width="4"/><line x1="29" y1="29" x2="42" y2="42" stroke="#fff" stroke-width="5" stroke-linecap="round"/><line x1="12" y1="19" x2="26" y2="19" stroke="#fff" stroke-width="3"/><line x1="19" y1="12" x2="19" y2="26" stroke="#fff" stroke-width="3"/></svg>
    </div>
    <div class="tile" style="background:linear-gradient(160deg,#9fb0a0,#6f6a52)" role="img" aria-label="Header pipe along a trench"></div>
    <div class="tile" style="background:linear-gradient(160deg,#a7a29a,#7d6e5c)" role="img" aria-label="Pump unit in a quarry"></div>
    <div class="tile" style="background:linear-gradient(160deg,#8f9a9b,#5d5e52)" role="img" aria-label="Hose discharging water"></div>
    <div class="tile" style="background:linear-gradient(160deg,#d8d8d8,#8a8a8a)" role="img" aria-label="Site inspection in black and white"></div>
    <div class="tile" style="background:linear-gradient(160deg,#5e5648,#a48c3a)" role="img" aria-label="Pump inside a shaft"></div>
    <div class="tile" style="background:linear-gradient(160deg,#bcc3c5,#5b5550)" role="img" aria-label="Geotextile dewatering bag"></div>
    <div class="tile" style="background:linear-gradient(160deg,#6e7f98,#a68468)" role="img" aria-label="Pipeline across dry land"></div>
  </div>
</section>

<section class="section partners">
  <h2 class="heading">Partners</h2><div class="rule"></div>
  <p class="sub">Lorem ipsum dolor sit amet, consectetur adipiscing elit. Praesent porttitor urna eu eleifend commodo.</p>
  <div class="logos"><span style="left:245px">SAMPLE</span><span style="left:481px">SAMPLE</span><span style="left:717px">SAMPLE</span><span style="left:952px">SAMPLE</span></div>
</section>

<section class="section cta">
  <h2>Lorem ipsum dolor sit amet, consectetur adipiscing elit. Praesent porttitor urna eu eleifend commodo.</h2>
  <p>Mauris a consectetur elit. Pellentesque pulvinar vitae sapien ac semper. Morbi interdum finibus eros in interdum. Aliquam eu facilisis orci, et semper velit. Morbi justo nisi, maximus id dignissim a, viverra ac tortor. Cras vel faucibus augue, sed viverra magna.</p>
  <div class="dark">CONTACT NOW</div>
</section>

<footer class="section footer" role="img" aria-label="Dim construction site backdrop">
  <div class="col" style="left:102px;width:200px"><h5>About our company</h5>Lorem ipsum dolor sit amet, consectetur adipiscing elit, sed do eiusmod tempor incididunt ut labore et dolore magna aliqua.</div>
  <div class="col" style="left:357px"><h5>Quick links</h5>Pumps<br>Generators<br>Dewatering<br>Plate Compactors<br>Light Towers</div>
  <div class="col" style="left:577px;width:230px"><h5>Twitter feed</h5>@lorem: Duis aute irure dolor in reprehenderit in voluptate velit esse cillum dolore eu fugiat.<br>@lorem: Duis aute irure dolor in reprehenderit in voluptate velit esse cillum dolore eu fugiat.</div>
  <div class="col" style="left:866px;width:260px"><h5>Contact us</h5>Have questions, comments or just want to say hello:<br><br>E: info@brackenfieldgoods.com<br>T: +1 (555) 014 0216<br>A: Sector # 4, Road # 12, Plot # 8</div>
  <div class="base"></div>
</footer>

</body>
</html>
```